LVP Roofing- Bold Web Design Project

We need a website design for a company that constructs and repairs commercial and residential roofing. They need a website design that looks clean, cutting edge, and can keep up with their competitors websites (Norvelle Crest, Fenwright Roofing Company, TZL Construction). They want to look experienced and "big" enough to handle large commercial projects. They also are striving for a professional and educational feel, and want to really articulate that they work with both residential/HOA and commercial clientele. They want a high conversion rate to their social media platforms and to another area of the site where they can fill out a form, so those areas should be emphasized.

Target Market(s)

Men and Women mainly between 25 and 65, typically in the higher income bracket (200,000+).

Industry/Entity Type

Residential

Requirements
Must have
• Landing page must have two separate but equally prominent buttons, directing the customers to a specific area of the site based on their need: commercial or residential. Clicking ether of these links will lead them to a welcome page for residential customers, or a welcome page for commercial clients.
-So must have 2 pages, a landing page and a welcome page that can be adapted for use as the commercial page and the residential page.
- A photo slider on the landing page
Nice to have
• -Color scheme should generally follow along with the colors used in the logo
-Professional, bold and modern.
Should not have
• -Avoid the "mom and pop" look
-Avoid the color red in the color scheme

```html
<!DOCTYPE html>
<html lang="en">
<head>
<meta charset="utf-8">
<title>LVP Roofing — Commercial and Residential Roofing Contractor</title>
<link rel="stylesheet" href="https://fonts.googleapis.com/css2?family=Cabin:wght@400;500;600;700&family=Tinos:wght@700&display=swap">
<style>
:root{
  --green:#9cc23a;
  --green-light:#c3e06a;
  --green-dark:#7fa421;
  --green-text:#8db82c;
  --green-pale:#e3f3b0;
  --hero-top:#cfe4a4;
  --hero-bottom:#b6d680;
  --ink:#111;
  --body:#222;
  --white:#fff;
  --footer:#1e1e1e;
  --badge:#6f7f5a;
}
*{box-sizing:border-box;margin:0;padding:0}
html,body{width:1114px;height:1200px;overflow:hidden;background:var(--white)}
body{position:relative;font-family:"Cabin",sans-serif;color:var(--body)}
.abs{position:absolute}

/* header */
.brand{left:97px;top:38px;font-size:44px;font-weight:700;color:#2b2b2b;line-height:1;letter-spacing:1px}
.brand-sub{left:97px;top:88px;font-size:20px;font-weight:700;color:#2b2b2b;letter-spacing:4px}
.call-box{left:756px;top:21px;width:262px;height:99px;border:1px solid #cfcfcf;border-radius:40px;text-align:center;background:linear-gradient(#fff,#f4f4f4)}
.call-label{margin-top:6px;font-size:15px;font-weight:700;color:var(--ink)}
.call-number{font-size:28px;color:var(--green-text);line-height:30px}
.search{position:absolute;left:34px;top:58px;width:200px;height:30px;border:1px solid #bbb;border-radius:6px;background:linear-gradient(#f4f4f4,#fff);font-size:14px;color:#888;padding:6px 9px;text-align:left}
.search svg{position:absolute;right:6px;top:6px}

/* nav */
.nav{left:0;top:133px;width:1114px;height:45px;background:linear-gradient(var(--green-light),var(--green-dark))}
.nav ul{list-style:none;display:flex;position:absolute;left:93px;top:0;height:45px}
.nav li{color:var(--white);font-size:15px;line-height:45px;padding:0 14px;border-right:1px solid rgba(255,255,255,.35)}
.nav li:last-child{border-right:0}

/* hero */
.hero-photo{left:0;top:178px;width:1114px;height:430px;background:linear-gradient(var(--hero-top),var(--hero-bottom))}
.hero-curve{left:0;top:178px}
.hero-title{left:0;top:216px;width:1114px;text-align:center;font-family:"Tinos",serif;font-size:26px;color:var(--ink)}
.hero-rule{left:185px;top:268px;width:745px;height:1px;background:#6b7a55}
.slide{border-radius:50%;background:linear-gradient(#d4ec8a,var(--green));box-shadow:0 8px 14px rgba(0,0,0,.2)}
.slide-photo{position:absolute;border-radius:50%;overflow:hidden;background:linear-gradient(#b9bfc4,#6e746f)}
.slide-label{position:absolute;left:0;width:100%;text-align:center;color:var(--white);background:linear-gradient(var(--green-light),var(--green-dark));border-top:3px solid #e9f6c0;font-weight:600}
.nav-btn{width:34px;height:34px;border-radius:50%;background:var(--white);box-shadow:0 1px 4px rgba(0,0,0,.4)}
.nav-btn svg{position:absolute;left:9px;top:9px}

/* welcome */
.welcome{left:95px;top:617px;width:595px}
.welcome h1{font-size:20px;font-weight:600;color:var(--ink);margin-bottom:5px}
.welcome p{font-size:13px;line-height:17px;margin-bottom:17px}
.more-link{left:520px;top:841px;width:158px;text-align:right;font-size:13px;font-weight:600;color:var(--green-text)}
.choice{left:753px;width:218px;height:114px}
.choice span{position:absolute;left:5px;top:44px;font-size:19px;font-weight:600;color:var(--white)}

/* partners */
.partners{left:93px;top:879px;width:925px;height:87px;background:var(--green-pale);border:1px solid #c9d9a2;display:flex;align-items:center;justify-content:space-around;padding:0 10px}
.badge{background:var(--badge);opacity:.85}

/* contact */
.contact-title{left:96px;top:1003px;font-size:15px;font-weight:600;color:var(--green-text)}
.contact-rule{left:96px;top:1029px;width:245px;border-top:1px dotted #999}
.contact-row{left:121px;font-size:13px;color:var(--ink)}
.footer-brand{left:432px;top:1050px;width:220px;text-align:center;font-size:36px;font-weight:700;color:#2b2b2b}

/* newsletter */
.newsletter{left:702px;top:992px;width:316px;height:150px;border-radius:15px;border:2px solid #d6e9a4;background:linear-gradient(var(--green),var(--green-light) 60%,#cfe78b)}
.news-title{position:absolute;left:74px;top:10px;font-size:26px;color:var(--white);font-weight:500}
.news-rule{position:absolute;left:74px;top:45px;width:210px;border-top:1px dotted rgba(255,255,255,.8)}
.news-sub{position:absolute;left:0;top:56px;width:100%;text-align:center;font-size:13px;font-weight:600;color:var(--white)}
.news-input{position:absolute;left:19px;top:81px;width:274px;height:26px;border-radius:13px;background:var(--white);border-top:2px solid #333;font-size:13px;color:#6a8a1e;padding:4px 10px}
.news-btn{position:absolute;left:101px;top:117px;width:116px;height:22px;background:#3a3a3a;border:1px solid #ddd;color:var(--white);font-size:13px;text-align:center;line-height:20px}

/* footer */
.footer{left:0;top:1158px;width:1114px;height:42px;background:var(--footer);color:var(--white);font-size:13px;font-weight:600}
.footer .copy{position:absolute;left:98px;top:11px}
.footer .links{position:absolute;right:95px;top:12px}
.footer .links span{padding:0 5px;border-right:1px solid #aaa}
.footer .links span:last-child{border-right:0;padding-right:0}
</style>
</head>
<body>

<header>
  <div class="abs brand">LVP</div>
  <div class="abs brand-sub">NETWORK</div>
  <div class="abs call-box">
    <div class="call-label">Call Us on:</div>
    <div class="call-number">123.123.1234</div>
    <div class="search">search
      <svg width="16" height="16" viewBox="0 0 16 16"><circle cx="6.5" cy="6.5" r="4.5" fill="none" stroke="#333" stroke-width="2"/><line x1="10" y1="10" x2="14" y2="14" stroke="#333" stroke-width="2.5"/></svg>
    </div>
  </div>
</header>

<nav class="abs nav">
  <ul>
    <li>Home</li><li>About Us</li><li>Roofing Systems</li><li>Roofing Services</li><li>Industry Expertise</li><li>Environmental Solutions</li><li>Safety</li><li>Portfolio</li>
  </ul>
</nav>

<section>
  <div class="abs hero-photo" role="img" aria-label="Faded photo of a large suburban house with trees, tinted green"></div>
  <svg class="abs hero-curve" width="1114" height="440" viewBox="0 0 1114 440">
    <path d="M0 300 Q557 420 1114 300 L1114 440 L0 440 Z" fill="#fff"/>
  </svg>
  <div class="abs hero-title">LVP Roofing Commercial and Residential roofing contractor</div>
  <div class="abs hero-rule"></div>

  <div class="abs slide" style="left:192px;top:298px;width:228px;height:228px">
    <div class="slide-photo" style="left:10px;top:10px;width:208px;height:208px" role="img" aria-label="Photo of a house with a grey metal roof">
      <div class="slide-label" style="top:168px;height:40px;font-size:13px;line-height:15px;padding-top:4px">Metal Roofing<br>System</div>
    </div>
  </div>
  <div class="abs slide" style="left:712px;top:298px;width:230px;height:230px">
    <div class="slide-photo" style="left:10px;top:10px;width:210px;height:210px;background:linear-gradient(#c9cbc8,#eceeed)" role="img" aria-label="Photo of a white single-ply flat roof">
      <div class="slide-label" style="top:166px;height:44px;font-size:13px;line-height:15px;padding-top:5px">Single-Ply<br>Roofs</div>
    </div>
  </div>
  <div class="abs slide" style="left:418px;top:303px;width:302px;height:302px">
    <div class="slide-photo" style="left:10px;top:10px;width:282px;height:282px;background:linear-gradient(#a8adad,#3e4241)" role="img" aria-label="Photo of roofers laying a built-up roof membrane">
      <div class="slide-label" style="top:225px;height:57px;font-size:17px;line-height:20px;padding-top:5px">Built-Up<br>Roofs</div>
    </div>
  </div>

  <div class="abs nav-btn" style="left:138px;top:391px"><svg width="16" height="16" viewBox="0 0 16 16"><path d="M8 3 L3 8 L8 13 M13 3 L8 8 L13 13" fill="none" stroke="#333" stroke-width="2"/></svg></div>
  <div class="abs nav-btn" style="left:960px;top:391px"><svg width="16" height="16" viewBox="0 0 16 16"><path d="M3 3 L8 8 L3 13 M8 3 L13 8 L8 13" fill="none" stroke="#333" stroke-width="2"/></svg></div>
</section>

<main>
  <div class="abs welcome">
    <h1>Welcome to LVP Roofing</h1>
    <p>Lorem Ipsum is simply dummy text of the printing and typesetting industry. Lorem Ipsum has been the industry's standard dummy text ever since the 1500s, when an unknown printer took a galley of type and scrambled it to make a type specimen book. It has survived not only five centuries.</p>
    <p>But also the leap into electronic typesetting, remaining essentially unchanged. It was popularised in the 1960s with the release of Letraset sheets containing Lorem Ipsum passages, and more recently with desktop publishing software like Aldus PageMaker including versions of Lorem Ipsum.</p>
    <p>Lorem Ipsum is simply dummy text of the printing and typesetting industry. Lorem Ipsum has been the industry's standard dummy text ever since the 1500s, when an unknown printer took a galley of type and scrambled it to make a type specimen book.</p>
  </div>
  <div class="abs more-link">- please click here.</div>

  <div class="abs choice" style="top:616px">
    <svg width="218" height="114" viewBox="0 0 218 114"><defs><linearGradient id="arrowFill" x1="0" y1="0" x2="0" y2="1"><stop offset="0" stop-color="#c6e26e"/><stop offset="1" stop-color="#8db52a"/></linearGradient></defs><path d="M0 16 H104 V0 L218 57 L104 114 V98 H0 Z" fill="url(#arrowFill)"/></svg>
    <span>Residential Customer</span>
  </div>
  <div class="abs choice" style="top:737px">
    <svg width="218" height="114" viewBox="0 0 218 114"><path d="M0 16 H104 V0 L218 57 L104 114 V98 H0 Z" fill="url(#arrowFill)"/></svg>
    <span>Commercial Customer</span>
  </div>

  <div class="abs partners" aria-label="Memberships and certifications">
    <div class="badge" style="width:64px;height:72px;border-radius:4px"></div>
    <div class="badge" style="width:48px;height:70px"></div>
    <div class="badge" style="width:96px;height:44px"></div>
    <div class="badge" style="width:70px;height:70px;background:#2f8a3c"></div>
    <div class="badge" style="width:90px;height:38px"></div>
    <div class="badge" style="width:92px;height:48px"></div>
    <div class="badge" style="width:92px;height:34px;background:#2b6a73"></div>
    <div class="badge" style="width:66px;height:66px;border-radius:50%;background:#1f3f46"></div>
    <div class="badge" style="width:92px;height:30px;background:#2f7f74"></div>
  </div>
</main>

<footer>
  <div class="abs contact-title">Contact Details:</div>
  <div class="abs contact-rule"></div>
  <svg class="abs" style="left:95px;top:1042px" width="22" height="16" viewBox="0 0 22 16"><path d="M2 5 Q11 -1 20 5 L17 8 L14 5 H8 L5 8 Z M5 9 H17 L19 15 H3 Z" fill="#555"/></svg>
  <div class="abs contact-row" style="top:1042px">123.123.1234</div>
  <div class="abs contact-row" style="top:1070px">123.123.1234</div>
  <svg class="abs" style="left:95px;top:1100px" width="20" height="13" viewBox="0 0 20 13"><rect width="20" height="13" fill="#7fa421"/><path d="M0 0 L10 7 L20 0" fill="none" stroke="#fff" stroke-width="1.5"/></svg>
  <div class="abs contact-row" style="top:1098px">Address comes here...</div>
  <div class="abs contact-row" style="top:1126px">Address comes here...</div>

  <div class="abs footer-brand">LVP Network</div>

  <div class="abs newsletter">
    <svg style="position:absolute;left:26px;top:4px" width="42" height="42" viewBox="0 0 42 42"><circle cx="21" cy="21" r="19" fill="#2f6fb5" stroke="#fff" stroke-width="2"/><rect x="10" y="14" width="22" height="15" fill="#fff"/><path d="M10 14 L21 23 L32 14" fill="none" stroke="#2f6fb5" stroke-width="1.5"/></svg>
    <div class="news-title">Newsletter Signup</div>
    <div class="news-rule"></div>
    <div class="news-sub">Subscribe Now and Get Lattest Updates...</div>
    <div class="news-input">Enter Email Address...</div>
    <div class="news-btn">Subscribe Now</div>
  </div>

  <div class="abs footer">
    <div class="copy">Copyright©2011 LVP NETWORK.</div>
    <div class="links"><span>Home</span><span>About Us</span><span>Roofing Systems</span><span>Roofing Services</span></div>
  </div>
</footer>

</body>
</html>
```